We need a book cover design for a fitness professional's guidebook to be a successful trainer. LA celebrity trainer offers 7 ideas that are designed to transform any fitness professional's career and life. The cover design we are into is attached an includes the image of a man who is half dressed in a business suit and half dressed in fitness gear. The back photo should demonstrate the four sphere's the book is designed around (also attached) and will be included on the back with a brief description of the material (included below) and a short bio and photo of the writer (attached) at the very bottom. We'd like the book to have a work book feel, or text book geometry to it. The brand colors are Black and Red. The final design should invoke the feeling of success, health and happiness.

Dimensions: 8 5/8 x 5 3/4

USE WEBSITE AS REFERENCE FOR BRAND COLORS AND DESIGNS:
BrenoVigor.net

BOOK TITLE:
RISING STRIDE
"A fitness professional's guidebook to be a successful trainer."

BACK COVER COPY:
Celebrity conditioning specialist and trainer consultant, Tavo Minardi, offers powerful ideas that are designed to transform every fitness professional's career and life. Reveal essential tools that every trainer and entrepreneur should know. Discover the deeper meaning of yourself and your career by working smarter rather than harder.

Find out how to create a brand, advertise it, and hone in on your market. Create buzz by landing magazine press. How to build celebrity clientele. Explore the world of multi-media projects. And finally, what to do when you reach your goals. This is an opportunity for trainer's to capture a share of the fitness industry’s vast $27B market. Fulfill your fullest earning potential while also understanding what the true meaning of success is, and how to achieve it. Learn what you love to do, what you do well, what the fitness industry needs and what it will pay for.

Aimed at the trainers who want to know the mistakes to avoid, and the habits to establish that will set them apart from the rest, Rising Stride is THE guidebook that has the power to take your career and life in the direction that will prepare you for continued success. Use these business ideas to promote your passive income, generate multiple streams of revenue and increase your investments, resulting in more freedom and access in the fitness industry and beyond. Let Rising Stride unleash your potential to be a successful trainer.

BACK AUTHOR BIO:
Los Angeles based celebrity trainer and trainer consultant, Tavo Minardi, CSCS, developed his very own “Ember” technique and fitness brand. Minardi’s clients include a mix of celebrities, professional athletes, musicians, fashion models, students, political figures and corporate professionals. Kelvo magazine described Minardi’s fitness DVD, TAVOMOVE, as “a workout you’ll look forward to”. Tavo was also the co-developer of a natural energy drink that increases energy and metabolism with an ancient Peruvian super food. Additionally backed by his finance and advertising education, Tavo has consulted several trainers and fitness brands to guide them to their maximum earning potential.

Target Market(s)

Fitness Industry/Trainers

Industry/Entity Type

Advertising

Requirements
Must have
• Consistent with website logo colors, shapes and fonts.

```html
<!DOCTYPE html>
<html lang="en">
<head>
<meta charset="utf-8">
<title>Rising Stride — Book Cover Spread</title>
<link href="https://fonts.googleapis.com/css2?family=Oswald:wght@700&family=PT+Sans:wght@400&family=Marcellus+SC&display=swap" rel="stylesheet">
<style>
  :root {
    --red: #ef4b4b;
    --black: #000000;
    --white: #ffffff;
    --ink: #1a1a1a;
    --photo-dark: #2a2a2a;
    --photo-mid: #6b6b6b;
  }
  * { box-sizing: border-box; margin: 0; padding: 0; }
  html, body {
    width: 1200px; height: 914px; overflow: hidden;
    background: var(--white);
  }
  .spread {
    position: relative; width: 1200px; height: 914px;
    display: flex;
  }

  /* Back cover */
  .back-cover {
    position: relative; width: 566px; height: 914px;
    background: var(--red); color: var(--white);
  }
  .back-copy {
    position: absolute; left: 20px; top: 16px; width: 528px;
    font-family: "PT Sans", sans-serif; font-size: 16px; line-height: 23px;
    text-align: justify;
  }
  .back-copy p + p { margin-top: 23px; }
  .author-band {
    position: absolute; left: 0; top: 558px; width: 566px; height: 287px;
    background: var(--black); padding: 20px 19px 0 13px;
  }
  .author-photo {
    float: left; width: 146px; height: 138px; margin: 0 12px 4px 0;
    background: linear-gradient(160deg, var(--photo-mid), var(--photo-dark));
  }
  .author-bio {
    font-family: "PT Sans", sans-serif; font-size: 11.6px; line-height: 20.5px;
    text-align: justify; color: var(--white);
  }
  .site-url {
    position: absolute; left: 0; bottom: 22px; width: 566px;
    text-align: center; font-family: "PT Sans", sans-serif;
    font-size: 17px; letter-spacing: 3px; color: var(--white);
  }

  /* Spine */
  .spine {
    position: relative; width: 57px; height: 914px; background: var(--black);
  }
  .spine-title, .spine-author {
    position: absolute; left: 50%; white-space: nowrap;
    transform-origin: 0 0; transform: rotate(90deg) translateY(-50%);
  }
  .spine-title {
    top: 24px; font-family: "Oswald", sans-serif; font-weight: 700;
    font-size: 44px; line-height: 1; color: var(--white); letter-spacing: 1px;
  }
  .spine-title .accent { color: var(--red); }
  .spine-author {
    top: 523px; font-family: "Marcellus SC", serif; font-size: 30px;
    line-height: 1; color: var(--white); letter-spacing: 2px;
  }

  /* Front cover */
  .front-cover {
    position: relative; width: 577px; height: 914px; background: var(--white);
  }
  .front-title {
    position: absolute; left: 0; top: 36px; width: 577px; text-align: center;
    font-family: "Oswald", sans-serif; font-weight: 700; font-size: 136px;
    line-height: 108px; letter-spacing: 1px;
  }
  .front-title .line-one { display: block; color: var(--ink); }
  .front-title .line-two { display: block; color: var(--red); }
  .hero-photo {
    position: absolute; left: 43px; top: 365px; width: 507px; height: 295px;
    background: radial-gradient(ellipse at 50% 60%, var(--photo-mid), var(--white) 72%);
  }
  .tagline {
    position: absolute; left: 0; top: 694px; width: 577px; text-align: center;
    font-family: "PT Sans", sans-serif; font-size: 29px; line-height: 33px;
    color: var(--ink);
  }
  .tagline-rule {
    position: absolute; left: 106px; top: 768px; width: 412px; height: 2px;
    background: var(--red);
  }
  .front-author {
    position: absolute; left: 0; top: 820px; width: 577px; text-align: center;
    font-family: "Marcellus SC", serif; font-size: 46px; letter-spacing: 3px;
    color: var(--ink);
  }
</style>
</head>
<body>
<div class="spread">
  <section class="back-cover">
    <div class="back-copy">
      <p>Celebrity conditioning specialist and trainer consultant, Tavo Minardi, offers powerful ideas that are designed to transform every fitness professional's career and life. Reveal essential tools that every trainer and entrepreneur should know. Discover the deeper meaning of yourself and your career by working smarter rather than harder.</p>
      <p>Find out how to create a brand, advertise it, and hone in on your market. Create buzz by landing magazine press. How to build celebrity clientele. Explore the world of multi-media projects. And finally, what to do when you reach your goals. This is an opportunity for trainer's to capture a share of the fitness industry’s vast $27B market. Fulfill your fullest earning potential while also understanding what the true meaning of success is, and how to achieve it. Learn what you love to do, what you do well, what the fitness industry needs and what it will pay for.</p>
      <p>Aimed at the trainers who want to know the mistakes to avoid, and the habits to establish that will set them apart from the rest, Rising Stride is THE guidebook that has the power to take your career and life in the direction that will prepare you for continued success. Use these business ideas to promote your passive income, generate multiple streams of revenue and increase your investments, resulting in more freedom and access in the fitness industry and beyond. Let Rising Stride unleash your potential to be a successful trainer.</p>
    </div>
    <div class="author-band">
      <div class="author-photo" role="img" aria-label="Portrait photo of the author, Tavo Minardi, seated against a city skyline"></div>
      <p class="author-bio">Los Angeles based celebrity trainer and trainer consultant, Tavo Minardi, CSCS, developed his very own “Ember” technique and fitness brand. Minardi’s clients include a mix of celebrities, professional athletes, musicians, fashion models, students, political figures and corporate professionals. Kelvo magazine described Minardi’s fitness DVD, TAVOMOVE, as “a workout you’ll look forward to”. Tavo was also the co-developer of a natural energy drink that increases energy and metabolism with an ancient Peruvian super food. Additionally backed by his finance and advertising education, Tavo has consulted several trainers and fitness brands to guide them to their maximum earning potential.</p>
    </div>
    <p class="site-url">www.brenovigor.net</p>
  </section>

  <section class="spine">
    <p class="spine-title">RISING<span class="accent">STRIDE</span></p>
    <p class="spine-author">Tavo Minardi</p>
  </section>

  <section class="front-cover">
    <h1 class="front-title"><span class="line-one">RISING</span><span class="line-two">STRIDE</span></h1>
    <div class="hero-photo" role="img" aria-label="Silhouetted trainer crouching to coach a client doing sit-ups with a medicine ball"></div>
    <p class="tagline">A fitness professional’s guidebook<br>to be a successful trainer</p>
    <div class="tagline-rule"></div>
    <p class="front-author">Tavo Minardi</p>
  </section>
</div>
</body>
</html>
```